Lumen Kinetics Web Design Project

We need to update our web design for our company. Lumen Kinetics™ is a series of Development (Training) Programs that we deliver both for the General Public as well as Corporate Business.

Much of the content needs a refresh but we are keen to get some thoughts now on design and layout, predominantly front page. Happy to take any comments on the content if you think that is relevant as well.

We might look to move the current video clip and bring a more generic 'inspirational' clip to the front page. A good example of this is www.mindcraftoz.example.au

Our courses have a very similar market to Gerald Whitcombe type courses ... both General Public and Corporate business.

Refer our website www.lumenkinetics.example.com

Target Market(s)

General Public as well as Corporate Business. Courses are designed for all. Gerald Whitcombe would be a good 'feel' for what we do.

Industry/Entity Type

Business

Requirements
Must have
• Must have a 'leading edge' type feel to it.
Must look professional.

```html
<!DOCTYPE html>
<html lang="en">
<head>
<meta charset="utf-8">
<title>Lumen Kinetics</title>
<link rel="stylesheet" href="https://fonts.googleapis.com/css2?family=Arimo:ital,wght@0,400;0,700;1,700&display=swap">
<style>
:root{
  --sky:#5cc3f2;
  --mist:#dcded8;
  --stone:#e8e9e4;
  --navy:#154d7c;
  --deep:#0e3457;
  --steel:#3a7ba8;
  --orange:#fb9a0a;
  --ink:#1a4a70;
  --body:#666;
  --quote:#8a8a86;
  --bright:#5bbcef;
}
*{margin:0;padding:0;box-sizing:border-box}
html,body{width:1200px;height:1000px;overflow:hidden;background:#fff;font-family:"Arimo",Arial,sans-serif}
.page{position:relative;width:1200px;height:1000px}
.abs{position:absolute}

.hero{left:0;top:0;width:1200px;height:185px;background:var(--mist)}
.hero-sky{left:0;top:0;width:1200px;height:20px;background:linear-gradient(90deg,#9fd5ef,#cfe9f6 30%,#6fb3de 80%,#a9d6ee)}
.hero-wave{left:0;top:172px}
.video-frame{left:120px;top:0;width:960px;height:76px;background:#eceeea;border-radius:0 0 8px 8px}
.video-area{left:140px;top:0;width:920px;height:57px;background:linear-gradient(100deg,#5fc4f6 0%,#74c9f3 55%,#cfe6f0 80%,#e4e9ea 100%)}
.video-shadow{left:170px;top:76px;width:860px;height:26px;background:radial-gradient(ellipse at top,rgba(0,0,0,.28),rgba(0,0,0,0) 70%)}
.tagline{left:0;top:118px;width:1205px;text-align:center;font-size:20px;color:var(--ink)}
.tagline sup,.band-title sup{font-size:10px;vertical-align:7px}

.intro{left:120px;top:225px;width:640px;font-size:15px;line-height:24px;color:var(--body)}
.intro a{color:var(--orange);font-weight:700;text-decoration:none}
.quote{left:780px;top:226px;width:300px;height:100px;background:var(--stone);border-radius:6px;display:flex;align-items:center;justify-content:center;text-align:center;font-size:18px;line-height:22px;font-style:italic;font-weight:700;color:var(--quote);padding:0 30px}
.quote-notch{left:812px;top:216px}

.band-title{left:120px;top:370px;width:960px;height:40px;background:var(--navy);border-radius:8px;color:#fff;font-size:22px;text-align:center;line-height:38px}
.band-shadow{left:200px;top:410px;width:800px;height:16px;background:radial-gradient(ellipse at top,rgba(0,0,0,.12),rgba(0,0,0,0) 70%)}
.lead{left:130px;top:427px;width:940px;text-align:center;font-size:15px;line-height:26px;color:var(--body)}

.audience{top:495px;width:141px;height:57px;border-radius:4px;color:#fff;font-weight:700;font-size:16px;line-height:19px;display:flex;align-items:center;justify-content:center;text-align:center}
.audience::before{content:"";position:absolute;left:63px;top:-6px;border:7px solid transparent;border-top:0;border-bottom:6px solid currentColor}
.audience.warm{background:var(--orange);color:#fff}
.audience.cool{background:var(--steel)}
.audience.warm::before{border-bottom-color:var(--orange)}
.audience.cool::before{border-bottom-color:var(--steel)}
.rule-shadow{left:120px;top:560px;width:960px;height:24px;background:linear-gradient(180deg,rgba(255,255,255,0),rgba(0,0,0,.05));border-radius:0 0 50% 50%/0 0 100% 100%}

.events{left:120px;top:596px;width:960px;height:100px;border-radius:8px 8px 0 0;background:linear-gradient(180deg,#e6e7e3,#fff)}
.events h2{position:absolute;left:30px;top:15px;font-weight:400;font-size:20px;color:var(--ink)}
.events p{position:absolute;left:30px;top:44px;font-size:16px;color:var(--body)}
.register{left:902px;top:626px;width:151px;height:37px;background:var(--bright);border-radius:4px;color:#fff;font-weight:700;font-size:17px;line-height:37px;padding-left:17px}
.register svg,.subscribe svg{position:absolute;top:50%;transform:translateY(-50%)}

.newsletter{left:0;top:730px;width:1200px;height:112px;background:var(--steel)}
.newsletter h2{position:absolute;left:0;top:14px;width:1198px;text-align:center;font-weight:400;font-size:20px;color:#fff}
.signup{left:120px;top:780px;width:960px;height:62px;background:var(--navy);border-radius:8px 8px 0 0}
.field{top:800px;width:250px;height:30px;background:#fff;border-radius:3px;font-size:14px;color:#888;line-height:30px;padding-left:8px}
.subscribe{left:950px;top:800px;width:110px;height:30px;background:var(--steel);border-radius:3px;color:#fff;font-weight:700;font-size:15px;line-height:30px;padding-left:13px}

.footer{left:0;top:840px;width:1200px;height:160px;background:var(--deep);border-top:8px solid #184d7a}
.social{top:868px;width:24px;height:24px;background:var(--steel);border-radius:2px}
.contact{left:265px;top:873px;font-size:13px;color:#fff;white-space:nowrap}
.contact b{font-weight:700}
.footer-rule{left:120px;top:910px;width:960px;height:1px;background:#2d6f9d}
.copyright{left:0;top:924px;width:1210px;text-align:center;font-size:11px;color:#5d9cc8}
</style>
</head>
<body>
<div class="page">
  <div class="abs hero"></div>
  <div class="abs hero-sky"></div>
  <div class="abs video-frame"></div>
  <div class="abs video-area" role="img" aria-label="Inspirational video clip with player controls"></div>
  <div class="abs video-shadow"></div>
  <svg class="abs hero-wave" width="1200" height="14" viewBox="0 0 1200 14" aria-hidden="true">
    <path d="M0 6 Q7.5 0 15 6 T30 6 T45 6 T60 6 T75 6 T90 6 T105 6 T120 6 T135 6 T150 6 T165 6 T180 6 T195 6 T210 6 T225 6 T240 6 T255 6 T270 6 T285 6 T300 6 T315 6 T330 6 T345 6 T360 6 T375 6 T390 6 T405 6 T420 6 T435 6 T450 6 T465 6 T480 6 T495 6 T510 6 T525 6 T540 6 T555 6 T570 6 T585 6 T600 6 T615 6 T630 6 T645 6 T660 6 T675 6 T690 6 T705 6 T720 6 T735 6 T750 6 T765 6 T780 6 T795 6 T810 6 T825 6 T840 6 T855 6 T870 6 T885 6 T900 6 T915 6 T930 6 T945 6 T960 6 T975 6 T990 6 T1005 6 T1020 6 T1035 6 T1050 6 T1065 6 T1080 6 T1095 6 T1110 6 T1125 6 T1140 6 T1155 6 T1170 6 T1185 6 T1200 6 V14 H0 Z" fill="#fff"/>
  </svg>
  <p class="abs tagline">Lumen Kinetics<sup>TM</sup> delivers leading edge workshops, semiars and products in a fun and interactive way</p>

  <p class="abs intro">Lorem ipsum dolor sit amet, consectetur adipisicing elit, sed do eiusmod tempor incididunt ut labore et dolore magna aliqua. Ut enim ad minim veniam, quis nostrud exercitation ullamco laboris nisi ut aliquip ex ea commodo consequat. Duis aute irure dolor in reprehenderit in voluptate velit esse cillum dolore eu fugiat nulla pariatur ... <a href="#">find out more about us ›</a></p>
  <svg class="abs quote-notch" width="22" height="11" viewBox="0 0 22 11" aria-hidden="true"><path d="M0 11 L11 0 L22 11 Z" fill="#e8e9e4"/></svg>
  <blockquote class="abs quote">If there is one thing you do this year ... make sure it’s Lumen Kinetics™</blockquote>

  <h2 class="abs band-title" style="font-weight:400">Experience Lumen Kinetics<sup>TM</sup> for yourself</h2>
  <div class="abs band-shadow"></div>
  <p class="abs lead">Lorem ipsum dolor sit amet, consectetur adipisicing elit, sed do eiusmod tempor incididunt ut labore et dolore magna aliqua. Ut enim ad minim veniam, quis nostrud exercitation ullamco laboris nisi ut aliquip ex ea commodo consequat duis aute irure dolor in reprehenderit.</p>

  <a class="abs audience warm" style="left:124px">For<br>Yourself</a>
  <a class="abs audience cool" style="left:286px">For Children<br>and Schools</a>
  <a class="abs audience warm" style="left:448px">For<br>Business</a>
  <a class="abs audience cool" style="left:610px">For<br>Animals</a>
  <a class="abs audience warm" style="left:772px">For<br>Community</a>
  <a class="abs audience cool" style="left:934px">For<br>Practitioners</a>
  <div class="abs rule-shadow"></div>

  <section class="abs events">
    <h2>Upcoming events</h2>
    <p>Register your interest now and we will send you all the information and dates as they are scheduled!</p>
  </section>
  <a class="abs register">Register Now<svg style="right:11px" width="6" height="10" viewBox="0 0 6 10"><path d="M0 0 L6 5 L0 10 Z" fill="#1f6fa3"/></svg></a>

  <section class="abs newsletter"><h2>Sign up to our newsletter</h2></section>
  <div class="abs signup"></div>
  <div class="abs field" style="left:140px">First Name</div>
  <div class="abs field" style="left:410px">Surname</div>
  <div class="abs field" style="left:680px">Email</div>
  <a class="abs subscribe">Subscribe<svg style="right:12px" width="6" height="10" viewBox="0 0 6 10"><path d="M0 0 L6 5 L0 10 Z" fill="#9cc6e2"/></svg></a>

  <footer class="abs footer"></footer>
  <span class="abs social" style="left:120px"></span>
  <span class="abs social" style="left:150px"></span>
  <span class="abs social" style="left:180px"></span>
  <span class="abs social" style="left:210px"></span>
  <p class="abs contact"><b>Lumen Kinetics .</b> PO Box 418 . Harbour Lane East . Vic 3999 . Australia &nbsp;. <b>Telephone:</b> +61 (3) 5550 1842 &nbsp;. &nbsp;<b>Mobile:</b> +61 (0) 400 555 217</p>
  <div class="abs footer-rule"></div>
  <p class="abs copyright">Copyright © 2013 Lumen Kinetics</p>
</div>
</body>
</html>
```